Car Wrap Design for Parquet Company

We are a parquet retailer and parquet laying company from Germany. We need a car wrap design for our van. It should have a noticeable design and so be modern and look premium. Enclosed we present you three favorite designs from other companys. We especially like favorite1. We like the theme wood in the design. We'd like to hear the follwing in the advertisement: - Over 25 years experience (more that 25 years of experience) - Birch to Wenge (our slogan) quality - www.Dielen-Warnke.example (our website) - 0913 - 72 15 904 (our telephone number) Our van is a Varlo K420 M3T3. Enclosed you find some pictures and the dimensions.
Colors
Designer to choose colors to be used in the design.
Look and feel
Each slider illustrates characteristics of the customer's brand and the style your logo design should communicate.

```html
<!DOCTYPE html>
<html lang="de">
<head>
<meta charset="utf-8">
<title>Dielen Warnke – Fahrzeugbeschriftung</title>
<link href="https://fonts.googleapis.com/css2?family=Oswald:wght@500&family=Libre+Baskerville&family=Exo+2:wght@500&display=swap" rel="stylesheet">
<style>
  :root{
    --bg:#ffffff;
    --wood-light-1:#e6bd7a;
    --wood-light-2:#d7a560;
    --wood-light-3:#c58c48;
    --wood-dark-1:#a9552b;
    --wood-dark-2:#8c3f1d;
    --wood-dark-3:#6e2a12;
    --seam:#8c6a3e;
    --brand:#86451f;
    --claim:#dcaa66;
    --slogan:#efc991;
    --trim:#2f2e31;
    --glass-1:#8a8a8e;
    --glass-2:#3a393d;
    --chrome:#ececee;
    --tail-red:#b01e48;
    --tail-orange:#f07a1e;
    --tyre:#555659;
    --rim:#ffffff;
  }
  html,body{margin:0;padding:0;width:1200px;height:1200px;overflow:hidden;background:var(--bg);}
  .canvas{display:block;width:1200px;height:1200px;}
  .brand-name{font-family:"Oswald",sans-serif;font-weight:500;fill:var(--brand);}
  .claim{font-family:"Oswald",sans-serif;font-weight:500;fill:var(--claim);}
  .slogan{font-family:"Libre Baskerville",serif;fill:var(--slogan);}
  .slogan-sub{font-family:"Libre Baskerville",serif;fill:var(--slogan);}
  .contact{font-family:"Exo 2",sans-serif;font-weight:500;fill:var(--claim);}
  .panel-seam{fill:none;stroke:var(--seam);stroke-width:2;opacity:.55;}
</style>
</head>
<body>
<svg class="canvas" viewBox="0 0 1920 1920" xmlns="http://www.w3.org/2000/svg">
  <defs>
    <linearGradient id="woodLight" x1="0" y1="0" x2="1" y2="0.6">
      <stop offset="0" stop-color="var(--wood-light-1)"/>
      <stop offset="0.45" stop-color="var(--wood-light-2)"/>
      <stop offset="0.7" stop-color="var(--wood-light-1)"/>
      <stop offset="1" stop-color="var(--wood-light-3)"/>
    </linearGradient>
    <linearGradient id="woodDark" x1="0" y1="0" x2="1" y2="0.5">
      <stop offset="0" stop-color="var(--wood-dark-2)"/>
      <stop offset="0.3" stop-color="var(--wood-dark-1)"/>
      <stop offset="0.65" stop-color="var(--wood-dark-2)"/>
      <stop offset="1" stop-color="var(--wood-dark-3)"/>
    </linearGradient>
    <linearGradient id="glass" x1="0" y1="0" x2="0" y2="1">
      <stop offset="0" stop-color="var(--glass-1)"/>
      <stop offset="1" stop-color="var(--glass-2)"/>
    </linearGradient>
    <linearGradient id="chrome" x1="0" y1="0" x2="1" y2="0">
      <stop offset="0" stop-color="#8d8d92"/>
      <stop offset="1" stop-color="var(--chrome)"/>
    </linearGradient>
    <clipPath id="bodyClip">
      <path d="M210 575 L1140 595 C1250 610 1320 640 1390 720 L1600 935 C1700 990 1830 1040 1850 1100 L1862 1300 L1690 1312 L1690 1295 A140 140 0 0 0 1420 1295 L1420 1300 L600 1282 L600 1270 A140 140 0 0 0 330 1270 L200 1272 L125 1140 L140 930 L160 630 Q170 575 210 575 Z"/>
    </clipPath>
  </defs>

  <g class="van">
    <g clip-path="url(#bodyClip)">
      <rect class="wood-light" x="100" y="560" width="1780" height="760" fill="url(#woodLight)" role="img" aria-label="Helle Holzmaserung, Birke, waagerecht"/>
      <path class="wood-dark" role="img" aria-label="Dunkle Holzmaserung, Wenge, als geschwungene Welle"
        d="M100 960 C220 910 380 870 500 865 C560 865 560 900 540 960 C525 1010 590 1010 700 960 C820 900 960 860 1060 895 C1120 920 1120 990 1135 1040 C1150 1070 1300 1070 1500 1068 C1700 1070 1820 1100 1880 1130 L1880 1330 L100 1330 Z"
        fill="url(#woodDark)"/>
      <g class="panel-seams">
        <path class="panel-seam" d="M660 585 L655 1290"/>
        <path class="panel-seam" d="M1128 600 C1118 700 1118 900 1125 1295"/>
        <path class="panel-seam" d="M1150 730 L1160 1270"/>
        <path class="panel-seam" d="M1492 900 L1500 1160"/>
        <path class="panel-seam" d="M200 590 C180 700 175 850 178 930"/>
      </g>
    </g>

    <rect x="230" y="935" width="425" height="20" fill="var(--trim)" transform="rotate(1.4 230 935)"/>
    <path d="M1005 530 L1030 590" stroke="#9a9a9e" stroke-width="9" stroke-linecap="round"/>
    <rect x="1020" y="586" width="45" height="10" rx="4" fill="#8a8a8e"/>

    <path d="M1180 752 L1330 775 L1440 895 L1485 990 L1235 955 C1205 950 1195 935 1192 905 Z" fill="url(#glass)" stroke="#5b3a1a" stroke-width="3"/>
    <path d="M1330 775 L1352 972" stroke="#5b3a1a" stroke-width="4"/>
    <path d="M1475 915 L1565 1005 L1500 1000 Z" fill="var(--glass-2)" stroke="#5b3a1a" stroke-width="3"/>
    <rect x="1437" y="882" width="38" height="105" rx="14" fill="url(#glass)" stroke="#777" stroke-width="3"/>
    <path d="M1375 752 L1400 748 L1605 940 L1575 942 Z" fill="url(#chrome)"/>
    <path d="M1705 1060 C1760 1058 1820 1075 1835 1100 L1830 1125 C1790 1125 1740 1115 1720 1100 Z" fill="url(#chrome)"/>

    <rect x="1008" y="1002" width="86" height="16" rx="8" fill="url(#chrome)"/>
    <rect x="1173" y="1010" width="86" height="16" rx="8" fill="url(#chrome)"/>

    <path d="M200 1140 L340 1140 L300 1190 L200 1190 Z" fill="var(--trim)"/>
    <path d="M590 1148 L1415 1165 L1385 1215 L650 1198 Z" fill="var(--trim)"/>
    <rect x="1198" y="1186" width="44" height="10" rx="4" fill="var(--tail-orange)"/>
    <path d="M1620 1160 L1850 1165 L1862 1300 L1690 1312 C1690 1230 1660 1190 1620 1160 Z" fill="var(--trim)"/>
    <path d="M125 1135 L225 1135 L225 1265 L130 1265 L118 1210 Z" fill="var(--trim)"/>
    <path d="M65 1248 L225 1250 L228 1275 L75 1268 Z" fill="var(--trim)"/>

    <path d="M152 940 C170 930 195 940 205 950 L205 1135 L148 1135 Z" fill="var(--tail-red)"/>
    <rect x="148" y="1068" width="40" height="64" fill="var(--tail-orange)"/>
    <rect x="152" y="1073" width="30" height="40" fill="#ffffff"/>

    <g class="wheel">
      <circle cx="462" cy="1292" r="112" fill="var(--tyre)" stroke="#999" stroke-width="3"/>
      <circle cx="462" cy="1292" r="70" fill="var(--rim)"/>
      <circle cx="462" cy="1292" r="42" fill="none" stroke="#222" stroke-width="44" stroke-dasharray="16 16.99"/>
      <circle cx="462" cy="1292" r="11" fill="#fff" stroke="#333" stroke-width="3"/>
    </g>
    <g class="wheel">
      <circle cx="1550" cy="1292" r="112" fill="var(--tyre)" stroke="#999" stroke-width="3"/>
      <circle cx="1550" cy="1292" r="70" fill="var(--rim)"/>
      <circle cx="1550" cy="1292" r="42" fill="none" stroke="#222" stroke-width="44" stroke-dasharray="16 16.99"/>
      <circle cx="1550" cy="1292" r="11" fill="#fff" stroke="#333" stroke-width="3"/>
    </g>
  </g>

  <g class="wordmark">
    <rect x="238" y="640" width="160" height="160" fill="var(--brand)"/>
    <text class="brand-name" x="450" y="683" font-size="54" textLength="515" lengthAdjust="spacing">DIELEN</text>
    <text class="brand-name" x="450" y="800" font-size="112" textLength="535" lengthAdjust="spacingAndGlyphs">WARNKE</text>
  </g>

  <text class="slogan" x="232" y="1055" font-size="34" textLength="400" lengthAdjust="spacing">Birke Nach Wenge</text>
  <text class="slogan-sub" x="232" y="1088" font-size="16" textLength="400" lengthAdjust="spacing">QUALITÄT</text>

  <g class="claim" font-size="50" text-anchor="end">
    <text x="985" y="992">ÜBER</text>
    <text x="985" y="1038">25 JAHRE</text>
    <text x="985" y="1084">ERFAHRUNG</text>
  </g>

  <text class="contact" x="1212" y="1106" font-size="28" textLength="243" lengthAdjust="spacing">0913 - 72 15 904</text>
  <text class="contact" x="700" y="1256" font-size="22" textLength="378" lengthAdjust="spacing">WWW.DIELEN-WARNKE.EXAMPLE</text>
</svg>
</body>
</html>
```